Stationary Design to Complement our Website

We would like template designed for word documents that we can use for headed paper. The template should complement the style of our website & incorporate our existing logo. https://www.velmorantravel.com/

The header and footer design should be sperate PNG or JPEG files that we can copy and paste into word header and footers. They should work on A4 & letter sized papers.

Note the main web colours are as follows:

Black
HEX code #2b2c2b
C=71 M=64 Y=64 K=65
RGB 43,44,43

Green
HEX code #116c49
C=88 M=33 Y=82 K=24
RGB 17,108,73

Current fonts are ALEO & Gilroy.

Fonts and colours in new design don't have to match website exactly but should be complementary.

Font styles to use
Serif

Requirements
Must have
• a simple design that complements our website.
Some kind of graphic on the top & some sort of graphic on the bottom. Not just plain logo on top.
designs that incorporate the clouds might look good
Can also incorporate 5* rate harbor rating
Should not have
• no photographs included on the design

```html
<!DOCTYPE html>
<html lang="en">
<head>
<meta charset="utf-8">
<title>Velmoran Travel – Headed Paper</title>
<link rel="stylesheet" href="https://fonts.googleapis.com/css2?family=Cinzel:wght@400&display=swap">
<style>
  :root {
    --brand-green: #116c49;
    --brand-black: #2b2c2b;
    --paper: #ffffff;
    --backdrop: #efefed;
    --cloud-white: #f7f9f3;
  }
  html, body {
    margin: 0;
    padding: 0;
    width: 1200px;
    height: 1000px;
    overflow: hidden;
    background: var(--backdrop);
  }
  .letterhead {
    position: absolute;
    left: 303px;
    top: 78px;
    width: 595px;
    height: 840px;
    background: var(--paper);
    overflow: hidden;
  }
  .header-sky {
    position: absolute;
    left: 0;
    top: 0;
    width: 100%;
    height: 62px;
    background: linear-gradient(to bottom,
      var(--cloud-white) 0%,
      var(--cloud-white) 25%,
      #dfe9e2 42%,
      #6fa58d 55%,
      var(--brand-green) 68%,
      var(--brand-green) 100%);
  }
  .brand {
    position: absolute;
    left: 36px;
    top: 80px;
    display: flex;
    align-items: flex-start;
    gap: 10px;
  }
  .brand-dot {
    width: 14px;
    height: 14px;
    margin-top: 2px;
    border-radius: 50%;
    background: var(--brand-green);
  }
  .brand-name {
    margin: 4px 0 0;
    font-family: "Cinzel", "Times New Roman", serif;
    font-weight: 400;
    font-size: 22px;
    line-height: 35px;
    letter-spacing: 0.2em;
    color: #161616;
  }
  .brand-name span { display: block; }
  .header-rule {
    position: absolute;
    left: 218px;
    top: 132px;
    width: 377px;
    height: 5px;
    background: linear-gradient(to right, rgba(17,108,73,0) 0%, rgba(17,108,73,0.45) 45%, var(--brand-green) 100%);
  }
  .footer-swoosh {
    position: absolute;
    left: 0;
    top: 800px;
    width: 384px;
    height: 12px;
  }
  .footer-emblems {
    position: absolute;
    left: 413px;
    top: 794px;
    width: 157px;
    height: 21px;
    border-radius: 3px;
    background: var(--brand-green);
  }
  .footer-band {
    position: absolute;
    left: 0;
    bottom: 0;
    width: 100%;
    height: 21px;
    background: var(--brand-green);
  }
</style>
</head>
<body>
  <main class="letterhead">
    <div class="header-sky" role="img" aria-label="Soft white clouds drifting over a green band"></div>

    <div class="brand">
      <div class="brand-dot"></div>
      <h1 class="brand-name"><span>Velmoran</span><span>Travel</span></h1>
    </div>
    <div class="header-rule"></div>

    <svg class="footer-swoosh" viewBox="0 0 384 12" aria-hidden="true">
      <path d="M0 0 H338 C358 0 372 5 384 12 H0 Z" fill="var(--brand-black)"/>
    </svg>
    <div class="footer-emblems" role="img" aria-label="Row of six small green clover emblems"></div>
    <div class="footer-band"></div>
  </main>
</body>
</html>
```